Tradeshow Banner Design (Qty2, 6'H x 2'W)

Brightwell Contractors is an Electrical, Fire Alarm, and Security Contracting company. For tradeshows, we would like 2 vertical Banners to put behind our booth. Our colors are Red, Grey & Black. I would like the Banners to be informative on what services we provide, with some appealing Graphic Design. (bwc-kmo.com)
Slogan: Safeguarding Communities Electrical, Fire & Security Solutions
Target Market(s)
Commercial Construction Clients
Industry/Entity Type
Electrical / Construction
Font styles to use
Other font styles liked:
- Aileron
Colors
EB3D1F
EC4F4E
F09395
F8D3D4
FCEDEE
Requirements
Must have
- Our Logo, Color Scheme, Brief Caption of the services we provide
Nice to have
- Appealing Imagery & a modern/simplistic design

```html
<!DOCTYPE html>
<html lang="en">
<head>
<meta charset="utf-8">
<title>Brightwell Contractors – Tradeshow Banners</title>
<link rel="stylesheet" href="https://fonts.googleapis.com/css2?family=Roboto:wght@400;500;700;900&display=swap">
<style>
  :root {
    --red: #EB3D1F;
    --red-soft: #EC4F4E;
    --pink: #F09395;
    --blush: #F8D3D4;
    --dark: #1d1d1f;
    --dark-2: #2b2b2e;
    --grey: #8c8c90;
    --white: #ffffff;
    --page: #f2f2f2;
  }
  * { margin: 0; padding: 0; box-sizing: border-box; }
  html, body { width: 831px; height: 1200px; overflow: hidden; background: var(--page); }
  body { position: relative; font-family: "Roboto", Arial, sans-serif; }

  .banner {
    position: absolute; top: 4px; width: 400px; height: 1192px;
    overflow: hidden; background: var(--dark);
  }
  .banner--left { left: 6px; }
  .banner--right { left: 425px; }
  .banner__shapes { position: absolute; inset: 0; }

  .brand {
    position: absolute; left: 0; right: 0; text-align: center;
  }
  .brand__mark {
    width: 110px; height: 110px; border-radius: 50%;
    background: var(--red); margin: 0 auto 14px;
  }
  .brand__name {
    font-weight: 700; font-size: 24px; color: var(--grey);
    text-transform: uppercase; letter-spacing: 1px; line-height: 1.1;
  }

  .headline {
    position: absolute; left: 0; right: 0; text-align: center;
    color: var(--red); font-weight: 900; font-size: 37px;
    line-height: 1.08; text-transform: uppercase;
  }
  .subline {
    position: absolute; left: 0; right: 0; text-align: center;
    color: var(--dark); font-weight: 500; font-size: 19px;
  }

  .photo { position: absolute; border-radius: 50%; border: 5px solid var(--white); }

  .web {
    position: absolute; left: 0; right: 0; text-align: center; color: var(--white);
  }
  .web__lead { font-size: 26px; font-weight: 500; }
  .web__url { font-size: 31px; font-weight: 700; margin-top: 12px; }

  .skyline {
    position: absolute; left: 0; top: 0; width: 400px; height: 330px;
    background: linear-gradient(180deg, #3f6f9c 0%, #7ea6c6 45%, #c9b89a 75%, #6b6f62 100%);
  }

  .services { position: absolute; left: 0; right: 0; top: 570px; list-style: none; text-align: center; }
  .service { height: 95px; color: var(--white); font-size: 17px; font-weight: 500; }
  .service svg { display: block; margin: 0 auto 8px; width: 44px; height: 44px; }
</style>
</head>
<body>

<!-- Left banner -->
<section class="banner banner--left">
  <svg class="banner__shapes" viewBox="0 0 400 1192" aria-hidden="true">
    <circle cx="250" cy="720" r="250" fill="var(--red)"/>
    <circle cx="250" cy="720" r="212" fill="var(--dark-2)"/>
    <path d="M0 0H400V560C330 470 210 440 0 455Z" fill="var(--white)"/>
  </svg>

  <div class="brand" style="top:70px">
    <div class="brand__mark"></div>
    <div class="brand__name">Brightwell<br>Contractors</div>
  </div>

  <h1 class="headline" style="top:282px">Safeguarding<br>Communities</h1>
  <p class="subline" style="top:378px">Electrical, Fire &amp; Security Solutions</p>

  <div class="photo" role="img" aria-label="Technician working on an electrical panel"
       style="left:40px;top:480px;width:120px;height:120px;background:linear-gradient(135deg,#6d7379,#2e3338);"></div>
  <div class="photo" role="img" aria-label="Security camera in a warehouse"
       style="left:150px;top:470px;width:230px;height:230px;background:linear-gradient(135deg,#b9bcc0,#5a5f66);"></div>
  <div class="photo" role="img" aria-label="Red fire alarm panel on a wall"
       style="left:60px;top:645px;width:135px;height:135px;background:linear-gradient(135deg,#c23a2a,#e8e1dc);"></div>
  <div class="photo" role="img" aria-label="Person using an access control keypad"
       style="left:190px;top:720px;width:165px;height:165px;background:linear-gradient(135deg,#e6e3df,#8d8782);"></div>
  <div class="photo" role="img" aria-label="Conference room with audio video system"
       style="left:75px;top:820px;width:130px;height:130px;background:linear-gradient(135deg,#d9cfc2,#6f6a63);"></div>

  <div class="web" style="top:1040px">
    <p class="web__lead">Visit</p>
    <p class="web__url">www.bwc-kmo.com</p>
  </div>
</section>

<!-- Right banner -->
<section class="banner banner--right">
  <div class="skyline" role="img" aria-label="Modern apartment buildings against a blue evening sky"></div>
  <svg class="banner__shapes" viewBox="0 0 400 1192" aria-hidden="true">
    <circle cx="260" cy="880" r="350" fill="none" stroke="var(--red)" stroke-width="30"/>
    <path d="M0 215C130 185 280 195 400 235V520C290 495 140 505 0 545Z" fill="var(--white)"/>
  </svg>

  <div class="brand" style="top:225px">
    <div class="brand__mark" style="width:90px;height:90px;margin-bottom:10px"></div>
    <div class="brand__name" style="font-size:21px">Brightwell<br>Contractors</div>
  </div>

  <h2 class="headline" style="top:385px">Quick, Efficient<br>Service</h2>
  <p class="subline" style="top:478px">Single-Point Solution Call Center</p>

  <ul class="services">
    <li class="service">
      <svg viewBox="0 0 44 44" aria-hidden="true">
        <circle cx="22" cy="18" r="10" fill="var(--red)"/>
        <rect x="17" y="29" width="10" height="7" rx="1.5" fill="var(--red)"/>
        <g stroke="var(--red)" stroke-width="2.5" stroke-linecap="round">
          <line x1="22" y1="2" x2="22" y2="5"/><line x1="6" y1="18" x2="9" y2="18"/>
          <line x1="35" y1="18" x2="38" y2="18"/><line x1="10" y1="7" x2="12" y2="9"/>
          <line x1="34" y1="7" x2="32" y2="9"/>
        </g>
      </svg>
      Electrical Installation &amp; Repair
    </li>
    <li class="service">
      <svg viewBox="0 0 44 44" aria-hidden="true">
        <path d="M22 4L36 9V21C36 30 30 37 22 40C14 37 8 30 8 21V9Z" fill="var(--red)"/>
        <path d="M15 22L20 27L29 17" fill="none" stroke="var(--dark)" stroke-width="3"/>
      </svg>
      Security Monitoring
    </li>
    <li class="service">
      <svg viewBox="0 0 44 44" aria-hidden="true">
        <circle cx="12" cy="32" r="4" fill="var(--red)"/>
        <path d="M10 20A14 14 0 0 1 24 34M10 10A24 24 0 0 1 34 34" fill="none" stroke="var(--red)" stroke-width="4" stroke-linecap="round"/>
      </svg>
      Fire Alarm Systems
    </li>
    <li class="service">
      <svg viewBox="0 0 44 44" aria-hidden="true">
        <g fill="var(--red)">
          <circle cx="12" cy="8" r="3"/><circle cx="22" cy="8" r="3"/><circle cx="32" cy="8" r="3"/>
          <circle cx="12" cy="18" r="3"/><circle cx="32" cy="18" r="3"/>
          <path d="M20 16H24V27L30 28C32 28.5 33 30 32.5 32L31 40H19L15 31L18 29L20 31Z"/>
        </g>
      </svg>
      Access Control
    </li>
    <li class="service">
      <svg viewBox="0 0 44 44" aria-hidden="true">
        <rect x="5" y="7" width="34" height="23" rx="2" fill="var(--red)"/>
        <rect x="19" y="30" width="6" height="6" fill="var(--red)"/>
        <rect x="13" y="36" width="18" height="3" fill="var(--red)"/>
        <path d="M19 13V24L27 18.5Z" fill="var(--dark)"/>
      </svg>
      Audio Video Systems
    </li>
  </ul>

  <div class="web" style="top:1060px">
    <p class="web__lead">More info at</p>
    <p class="web__url">www.bwc-kmo.com</p>
  </div>
</section>

</body>
</html>
```